Small business updating business cards

We have already updated our logo via Pixel Forum and downloaded it (hopefully) for you to use. Now an updated set of business cards for Neil Pollard and Stuart Pollard are also needed... we are also hoping that a copy of our outdated business card designs have uploaded successfully as Microsoft Publisher files. Our Strength Through Unity motto has died a slow death so we are hoping to remove it (and other superfluous lingo if the graphic covers the idea) and instead opt for a fancy graphic (?) on the second side of the card that really reflects our desire to obtain product / haulage from Road Transport / Yard Operators and convert legs of their haulage to rail freight where profitable (bulk haulage / containterised etc). Can you help us look larger, bolder and more robust than we really are (two man show)?
Target Market(s)
Transport Industry
Industry/Entity Type
Business
Contact Information for Business Card
Card details for both N Pollard and S Pollard have been uploaded on the publisher files
Colors
Designer to choose colors to be used in the design.
Requirements
Must have
- Similar theme both sides of card
Should not have
- Black on one side white on the other

```html
<!DOCTYPE html>
<html lang="en">
<head>
<meta charset="UTF-8">
<title>Railvane business cards</title>
<link href="https://fonts.googleapis.com/css2?family=Roboto:wght@400;700&display=swap" rel="stylesheet">
<style>
  :root {
    --page: #e6e7e9;
    --card-dark: #4a4a4c;
    --card-light: #ffffff;
    --teal: #2b8ea6;
    --gold: #caa01c;
    --white: #ffffff;
    --shadow: rgba(0,0,0,0.25);
  }
  * { margin: 0; padding: 0; box-sizing: border-box; }
  html, body {
    width: 1200px; height: 900px; overflow: hidden;
    background: var(--page);
    font-family: "Roboto", Arial, sans-serif;
  }
  .canvas { position: relative; width: 1200px; height: 900px; }
  .card {
    position: absolute; left: 250px; width: 700px; height: 400px;
    overflow: hidden; box-shadow: 0 10px 28px var(--shadow);
  }
  .card--back { top: 35px; background: linear-gradient(160deg, #5a5a5c, var(--card-dark)); }
  .card--front { top: 465px; background: var(--card-light); }
  .brand-name {
    position: absolute; font-weight: 700; letter-spacing: 1px; white-space: nowrap;
  }
  .card--back .brand-name {
    left: 0; right: 0; top: 160px; text-align: center;
    font-size: 76px; color: var(--gold);
  }
  .card--front .brand-name {
    left: 400px; top: 165px; font-size: 58px; color: var(--teal);
  }
  .front-art { position: absolute; inset: 0; }
  .contact {
    position: absolute; left: 48px; top: 150px; color: var(--white);
  }
  .contact__name { font-size: 22px; font-weight: 700; }
  .contact__title { font-size: 16px; margin-top: 2px; }
  .contact__address { font-size: 14px; line-height: 19px; margin-top: 26px; }
  .contact__list { list-style: none; margin-top: 10px; font-size: 14px; line-height: 20px; }
  .contact__list li { display: flex; align-items: center; gap: 8px; }
  .contact__list svg { width: 13px; height: 13px; fill: var(--white); flex: none; }
</style>
</head>
<body>
<div class="canvas">
  <section class="card card--back">
    <div class="brand-name">Railvane</div>
  </section>

  <section class="card card--front">
    <svg class="front-art" viewBox="0 0 700 400" width="700" height="400" aria-hidden="true">
      <defs>
        <linearGradient id="panelGradient" x1="0" y1="1" x2="1" y2="0">
          <stop offset="0" stop-color="#2b8ea6"/>
          <stop offset="0.45" stop-color="#8fa65a"/>
          <stop offset="0.75" stop-color="#caa01c"/>
        </linearGradient>
      </defs>
      <path d="M0 0 H248 Q262 290 445 400 H0 Z" fill="url(#panelGradient)"/>
      <path d="M256 0 Q270 288 452 400" fill="none" stroke="var(--teal)" stroke-width="12"/>
      <path d="M256 0 Q270 288 452 400" fill="none" stroke="var(--white)" stroke-width="12" stroke-dasharray="2 34"/>
    </svg>

    <div class="brand-name">Railvane</div>

    <div class="contact">
      <div class="contact__name">Neil Pollard</div>
      <div class="contact__title">President</div>
      <div class="contact__address">27 Harbour Siding Road<br>Eastfield, NY 10470</div>
      <ul class="contact__list">
        <li><svg viewBox="0 0 16 16"><path d="M3 1h3l1 4-2 1a9 9 0 0 0 5 5l1-2 4 1v3a2 2 0 0 1-2 2A13 13 0 0 1 1 3a2 2 0 0 1 2-2z"/></svg>555 0142 7781</li>
        <li><svg viewBox="0 0 16 16"><path d="M4 0h8a1 1 0 0 1 1 1v14a1 1 0 0 1-1 1H4a1 1 0 0 1-1-1V1a1 1 0 0 1 1-1zm1 2v10h6V2zm3 11a1 1 0 1 0 0 2 1 1 0 0 0 0-2z"/></svg>555 0193 4426</li>
        <li><svg viewBox="0 0 16 16"><path d="M4 0h7v5H4zM1 6h14v7h-3v3H4v-3H1zm4 5v3h6v-3z"/></svg>555 0167 2039</li>
        <li><svg viewBox="0 0 16 16"><path d="M0 3h16v10H0zm1 1v1l7 4 7-4V4z"/></svg>neil@railvane.com</li>
        <li><svg viewBox="0 0 16 16"><circle cx="8" cy="8" r="7"/></svg>www.railvane.com</li>
      </ul>
    </div>
  </section>
</div>
</body>
</html>
```